Quorvex business card design

create modern and tech looking business card that is clean but effectively communciates that we are a cloud communications company.
Should have at minimum:
Employee Name
Postion
Phone Number
Email
website
create modern and tech looking business card that is clean but effectively communciates that we are a cloud communications company. We have two logo color schemes (attached) so would like to see designs both ways
Should have at minimum:
Employee Name
Postion
Phone Number
Email
website

```html
<!DOCTYPE html>
<html lang="en">
<head>
<meta charset="UTF-8">
<title>Quorvex Business Card</title>
<link rel="stylesheet" href="https://fonts.googleapis.com/css2?family=Roboto:wght@400;500&display=swap">
<style>
  :root {
    --backdrop: #ababab;
    --card: #f1f1f1;
    --purple: #5a2a88;
    --teal: #2bb0cf;
    --ink: #3f3f3f;
    --muted: #4a4a4a;
  }
  * { box-sizing: border-box; margin: 0; padding: 0; }
  html, body {
    width: 1200px;
    height: 576px;
    overflow: hidden;
    background: var(--backdrop);
    font-family: "Roboto", sans-serif;
  }
  .stage {
    position: relative;
    width: 1200px;
    height: 576px;
  }
  .card {
    position: absolute;
    width: 484px;
    height: 292px;
    background: var(--card);
    border-radius: 12px;
  }
  .card--front { left: 82px; top: 139px; }
  .card--back { left: 602px; top: 139px; }

  .brand {
    position: absolute;
    display: flex;
    align-items: center;
    gap: 12px;
  }
  .brand__mark {
    background: var(--purple);
  }
  .brand__name {
    font-weight: 500;
    color: var(--ink);
    letter-spacing: 0.06em;
    text-transform: uppercase;
    line-height: 1;
  }
  .card--front .brand {
    left: 100px;
    top: 122px;
  }
  .card--front .brand__mark { width: 40px; height: 40px; }
  .card--front .brand__name { font-size: 40px; }

  .card--back .brand {
    left: 262px;
    top: 207px;
    gap: 8px;
  }
  .card--back .brand__mark { width: 24px; height: 24px; }
  .card--back .brand__name { font-size: 24px; }

  .person {
    position: absolute;
    left: 28px;
    top: 38px;
  }
  .person__name {
    font-size: 21px;
    font-weight: 500;
    color: var(--purple);
    line-height: 1.1;
  }
  .person__role {
    margin-top: 4px;
    font-size: 11px;
    color: var(--muted);
  }

  .contact {
    position: absolute;
    left: 28px;
    top: 207px;
    list-style: none;
  }
  .contact__item {
    display: flex;
    align-items: center;
    gap: 9px;
    height: 18px;
    font-size: 12px;
    color: var(--ink);
  }
  .contact__icon {
    width: 12px;
    height: 12px;
    fill: var(--purple);
    flex: none;
  }
  .contact__accent { color: var(--teal); }
</style>
</head>
<body>
<main class="stage">
  <section class="card card--front" aria-label="Card front">
    <div class="brand">
      <span class="brand__mark"></span>
      <span class="brand__name">Quorvex</span>
    </div>
  </section>

  <section class="card card--back" aria-label="Card back">
    <div class="person">
      <h1 class="person__name">Daniel Reyes</h1>
      <p class="person__role">Managing Director</p>
    </div>

    <ul class="contact">
      <li class="contact__item">
        <svg class="contact__icon" viewBox="0 0 12 12" aria-hidden="true">
          <path d="M1 3.2C1 2 2 1.5 6 1.5s5 .5 5 1.7v1H8.4V3.4H3.6v.8H1z"/>
          <path d="M3.2 5h5.6l2 3v2.5H1.2V8z"/>
        </svg>
        <span>1800-555-0147</span>
      </li>
      <li class="contact__item">
        <svg class="contact__icon" viewBox="0 0 12 12" aria-hidden="true">
          <path d="M1 2.5h10v7H1z M1.8 3.3 6 6.5l4.2-3.2z" fill-rule="evenodd"/>
        </svg>
        <span>dreyes@quorvexmail.com</span>
      </li>
      <li class="contact__item">
        <svg class="contact__icon" viewBox="0 0 12 12" aria-hidden="true">
          <circle cx="6" cy="6" r="4.8" fill="none" stroke="#5a2a88" stroke-width="1.1"/>
          <ellipse cx="6" cy="6" rx="2" ry="4.8" fill="none" stroke="#5a2a88" stroke-width="1"/>
          <path d="M1.2 6h9.6" stroke="#5a2a88" stroke-width="1"/>
        </svg>
        <span>www.<span class="contact__accent">quorvexcloud</span>.com</span>
      </li>
    </ul>

    <div class="brand">
      <span class="brand__mark"></span>
      <span class="brand__name">Quorvex</span>
    </div>
  </section>
</main>
</body>
</html>
```